Varnell Consulting needs a business card design

Varnell Consulting is a small business that consults and trains Australia wide in Workplace Health and Safety, Environment and Quality Management Systems.

Clients are typically smaller businesses with 50 to 200 employees but there are some large clients.

Communication is often by email, although mobile is used as well.

Varnell Consulting
47 Tessock Downs Road
Tarrowby, NSW 2871
0438 291 604

```html
<!DOCTYPE html>
<html lang="en">
<head>
<meta charset="utf-8">
<title>Varnell Consulting – Business Card</title>
<link href="https://fonts.googleapis.com/css2?family=Open+Sans:wght@400;600;700&display=swap" rel="stylesheet">
<style>
  :root {
    --page-bg: #e6e8ee;
    --card-white: #f7f7f8;
    --navy: #1f3577;
    --navy-deep: #1a2c66;
    --band-blue: #3f6db4;
    --band-light: #6f93cf;
    --text-on-blue: #ffffff;
    --text-soft: #e4ebf7;
  }
  * { margin: 0; padding: 0; box-sizing: border-box; }
  html, body {
    width: 1200px; height: 800px; overflow: hidden;
    background: var(--page-bg);
    font-family: "Open Sans", Arial, sans-serif;
  }
  .card {
    position: absolute; left: 150px; top: 125px;
    width: 900px; height: 550px;
    background: var(--card-white);
    box-shadow: 0 12px 36px rgba(20, 30, 60, 0.22);
    overflow: hidden;
  }
  .brand {
    position: absolute; left: 110px; top: 150px;
    display: flex; align-items: center; gap: 22px;
  }
  .brand-dot {
    width: 46px; height: 46px; border-radius: 50%;
    background: var(--navy);
  }
  .brand-name {
    font-weight: 700; font-size: 58px; letter-spacing: 0.5px;
    color: var(--navy); line-height: 1;
  }
  .info-band {
    position: absolute; left: 0; right: 0; top: 330px; bottom: 0;
    background: linear-gradient(100deg, var(--band-light) 0%, var(--band-blue) 45%, var(--navy-deep) 100%);
  }
  .info-band::before {
    content: ""; position: absolute; left: 0; right: 0; top: 0; height: 92px;
    background: linear-gradient(90deg, rgba(31,53,119,0.55), rgba(26,44,102,0.95));
  }
  .holder {
    position: absolute; left: 600px; top: 346px; color: var(--text-on-blue);
  }
  .holder-name { font-weight: 700; font-size: 28px; letter-spacing: 0.5px; line-height: 1.2; }
  .holder-role { font-weight: 400; font-size: 22px; line-height: 1.2; }
  .address {
    position: absolute; left: 80px; top: 455px;
    color: var(--text-soft); font-size: 22px; line-height: 1.45;
  }
  .divider {
    position: absolute; left: 330px; top: 440px; width: 2px; height: 70px;
    background: var(--text-on-blue);
  }
  .contact {
    position: absolute; left: 352px; top: 432px;
    list-style: none; color: var(--text-on-blue); font-size: 22px;
  }
  .contact li { display: flex; align-items: center; gap: 10px; line-height: 1.55; }
  .contact svg { width: 22px; height: 22px; flex: none; }
</style>
</head>
<body>
  <div class="card">
    <div class="brand">
      <span class="brand-dot"></span>
      <span class="brand-name">Varnell Consulting</span>
    </div>

    <div class="info-band"></div>

    <div class="holder">
      <div class="holder-name">ROWAN VARNELL</div>
      <div class="holder-role">Manager</div>
    </div>

    <div class="address">
      47 Tessock Downs Road<br>
      Tarrowby, NSW 2871
    </div>

    <div class="divider"></div>

    <ul class="contact">
      <li>
        <svg viewBox="0 0 24 24" aria-hidden="true">
          <circle cx="12" cy="12" r="11" fill="none" stroke="#fff" stroke-width="1.6"/>
          <path d="M8.3 6.5l2 2.3-1.2 1.4c.8 1.7 2 2.9 3.7 3.7l1.4-1.2 2.3 2-1 1.8c-4.2-.5-8-4.3-8.5-8.5z" fill="#fff"/>
        </svg>
        0438 291 604
      </li>
      <li>
        <svg viewBox="0 0 24 24" aria-hidden="true">
          <circle cx="12" cy="12" r="11" fill="none" stroke="#fff" stroke-width="1.6"/>
          <rect x="6.5" y="8" width="11" height="8" rx="1" fill="#fff"/>
          <path d="M6.8 8.4L12 12.4l5.2-4" fill="none" stroke="#3f6db4" stroke-width="1.2"/>
        </svg>
        r.varnell@mailbox.com.au
      </li>
    </ul>
  </div>
</body>
</html>
```